Redesign existing website.

I need a holidayhouse webdisain. Please review existing website: www.vaskemetsa.ee
I want to keep my logo.
Target Market(s)
Nature and sea enjoying holidaymakers, aged 30 to 70
Requirements
Must have
- 3 languages (English, Russian and Estonian)

```html
<!DOCTYPE html>
<html lang="et">
<head>
<meta charset="utf-8">
<title>Vaskemetsa Puhkemaja</title>
<link rel="stylesheet" href="https://fonts.googleapis.com/css2?family=Montserrat:wght@300;400;600;700&display=swap">
<style>
  :root {
    --page-bg: #f3f6c6;
    --brand-green: #00956f;
    --brand-green-dark: #00765a;
    --text-body: #4a4a3e;
    --white: #ffffff;
    --dot-active: #1aa3e8;
  }
  * { margin: 0; padding: 0; box-sizing: border-box; }
  html, body { width: 1200px; height: 1039px; overflow: hidden; }
  body {
    position: relative;
    background: var(--page-bg);
    font-family: "Montserrat", sans-serif;
    color: var(--text-body);
  }
  .abs { position: absolute; }

  /* Language switcher */
  .lang-switch { top: 30px; left: 848px; width: 220px; height: 44px; }
  .lang-item { position: absolute; top: 0; text-align: center; }
  .lang-flag { display: block; margin: 0 auto 6px; }
  .lang-label {
    font-size: 14px; font-weight: 700; color: var(--brand-green); white-space: nowrap;
  }

  /* Ribbon navigation */
  .ribbon-tail { top: 109px; }
  .main-nav {
    top: 79px; left: 136px; width: 929px; height: 63px;
    background: var(--brand-green);
  }
  .nav-link {
    position: absolute; top: 20px;
    transform: translateX(-50%);
    font-size: 17px; font-weight: 700; color: var(--white);
    text-decoration: none; white-space: nowrap;
  }
  .brand {
    position: absolute; left: 50%; top: -36px;
    transform: translateX(-50%);
    width: 124px; height: 124px;
    display: flex; flex-direction: column; align-items: center; justify-content: center;
    gap: 6px;
  }
  .brand-mark {
    width: 14px; height: 14px; border-radius: 50%; background: var(--white);
  }
  .brand-name {
    font-size: 14px; font-weight: 700; color: var(--white);
    text-align: center; line-height: 1.25; letter-spacing: 0.5px;
  }

  /* Hero */
  .hero {
    top: 142px; left: 157px; width: 885px; height: 325px;
    background: linear-gradient(180deg, #79b8e8 0%, #a9cfe3 28%, #d9d4c4 48%, #b58a68 62%, #6f8b3f 82%, #486b2b 100%);
  }
  .hero-shadow {
    top: 460px; left: 200px; width: 800px; height: 34px;
    border-radius: 50%;
    background: radial-gradient(ellipse at center, rgba(70,80,40,0.45) 0%, rgba(70,80,40,0) 70%);
  }
  .slider-dots { top: 433px; left: 560px; display: flex; gap: 8px; }
  .slider-dot { width: 14px; height: 14px; border-radius: 50%; background: var(--white); }
  .slider-dot.is-active { background: var(--dot-active); }

  /* Content */
  .section-title {
    font-size: 24px; font-weight: 400; color: var(--brand-green);
  }
  .welcome-title { top: 506px; left: 166px; }
  .welcome-text { top: 553px; left: 166px; width: 572px; }
  .welcome-text p {
    font-size: 12.6px; font-weight: 400; line-height: 22.2px; margin-bottom: 22px;
  }
  .gallery-title { top: 506px; left: 756px; }
  .gallery-preview {
    top: 554px; left: 757px; width: 277px; height: 202px;
    background: linear-gradient(135deg, #d9d6cf 0%, #8c6a52 38%, #7d3b2e 62%, #3c2e2a 100%);
  }
  .gallery-arrow { position: absolute; top: 86px; }

  /* Footer */
  .site-footer {
    top: 794px; left: 157px; width: 885px; height: 245px;
    background: var(--brand-green); color: var(--white);
  }
  .footer-links { position: absolute; top: 42px; list-style: none; }
  .footer-links li { font-size: 13px; line-height: 22.3px; }
  .footer-contact { position: absolute; top: 42px; left: 410px; font-size: 13px; line-height: 21.5px; }
  .footer-heading { font-size: 12.5px; font-weight: 700; letter-spacing: 0.5px; margin-bottom: 8px; }
  .social { position: absolute; top: 42px; left: 691px; }
  .social-icons { display: flex; gap: 12px; margin-top: 14px; }
  .social-icon { width: 20px; height: 20px; border-radius: 50%; background: var(--white); }
  .copyright {
    position: absolute; top: 207px; left: 0; width: 885px; text-align: center;
    font-size: 13px;
  }
</style>
</head>
<body>

  <div class="abs lang-switch">
    <div class="lang-item" style="left:0;width:60px;">
      <svg class="lang-flag" width="22" height="15" viewBox="0 0 22 15" aria-hidden="true">
        <rect width="22" height="15" fill="#1d3a8a"/>
        <path d="M0 0L22 15M22 0L0 15" stroke="#fff" stroke-width="3"/>
        <path d="M0 0L22 15M22 0L0 15" stroke="#c8102e" stroke-width="1"/>
        <path d="M11 0V15M0 7.5H22" stroke="#fff" stroke-width="4.5"/>
        <path d="M11 0V15M0 7.5H22" stroke="#c8102e" stroke-width="2.5"/>
      </svg>
      <span class="lang-label">English&nbsp;&nbsp;|</span>
    </div>
    <div class="lang-item" style="left:80px;width:60px;">
      <svg class="lang-flag" width="22" height="15" viewBox="0 0 22 15" aria-hidden="true">
        <rect width="22" height="5" fill="#fff"/>
        <rect y="5" width="22" height="5" fill="#1c57a5"/>
        <rect y="10" width="22" height="5" fill="#d52b1e"/>
      </svg>
      <span class="lang-label">Russian</span>
    </div>
    <div class="lang-item" style="left:146px;width:76px;">
      <svg class="lang-flag" width="22" height="15" viewBox="0 0 22 15" aria-hidden="true">
        <rect width="22" height="15" fill="#c60b1e"/>
        <rect y="4" width="22" height="7" fill="#ffc400"/>
      </svg>
      <span class="lang-label">| Estonian</span>
    </div>
  </div>

  <svg class="abs ribbon-tail" style="left:109px;" width="50" height="56" viewBox="0 0 50 56" aria-hidden="true">
    <polygon points="0,2 48,2 48,56 0,56 14,28" fill="var(--brand-green)"/>
    <polygon points="27,33 48,33 48,56" fill="var(--brand-green-dark)"/>
  </svg>
  <svg class="abs ribbon-tail" style="left:1041px;" width="50" height="56" viewBox="0 0 50 56" aria-hidden="true">
    <polygon points="50,2 2,2 2,56 50,56 36,28" fill="var(--brand-green)"/>
    <polygon points="23,33 2,33 2,56" fill="var(--brand-green-dark)"/>
  </svg>

  <nav class="abs main-nav">
    <a class="nav-link" href="#" style="left:105px;">Introduction</a>
    <a class="nav-link" href="#" style="left:231px;">Pricing</a>
    <a class="nav-link" href="#" style="left:336px;">Gallery</a>
    <div class="brand">
      <span class="brand-mark"></span>
      <span class="brand-name">VASKEMETSA<br>PUHKEMAJA</span>
    </div>
    <a class="nav-link" href="#" style="left:637px;">Location</a>
    <a class="nav-link" href="#" style="left:752px;">Contact</a>
    <a class="nav-link" href="#" style="left:853px;">Picks</a>
  </nav>

  <div class="abs hero-shadow"></div>
  <div class="abs hero" role="img" aria-label="Photo of the two-storey holiday house with red tiled roof, white walls and stone base, surrounded by lawn and trees"></div>
  <div class="abs slider-dots">
    <span class="slider-dot is-active"></span>
    <span class="slider-dot"></span>
    <span class="slider-dot"></span>
    <span class="slider-dot"></span>
  </div>

  <h1 class="abs section-title welcome-title">Welcome to Vaskemetsa</h1>
  <div class="abs welcome-text">
    <p>Majutus 5-le puhkajale. Teid ootab mugav 2 magamistoaga puhkemaja. Asume põhjarannikul, Juminda poolsaarel, Kivi külas, Lahemaa rahvuspargis. Tallinnast vaid 61 km kaugusel. Kivi on sobiv koht mõnusaks, rahulikuks puhkuseks. Sillerdavat merd ja kauneid päikeseloojanguid võib nautida lausa maja aknast. Või veel parem – jalutad randa ja istud päevapäikese poolt kuumaks köetud kivile. Meie maja vastas olev rand on kivine, väikesele liivarannale 100m. Lahemaa toredad terviserajad on lähedal.</p>
    <p>Alumisel korrusel elutuba kamina ja kööginurgaga. Kööginurgas kõik vajalik toidu valmistamiseks - elektripliit, nõudepesumasin, mikrolaineahi, külmik, kohvimasin, veekeetja, nõud.</p>
  </div>

  <h2 class="abs section-title gallery-title">Gallery</h2>
  <div class="abs gallery-preview" role="img" aria-label="Photo of the living room with dining table, kitchen corner and lit fireplace">
    <svg class="gallery-arrow" style="left:14px;" width="22" height="34" viewBox="0 0 22 34" aria-hidden="true">
      <polyline points="18,3 4,17 18,31" fill="none" stroke="#fff" stroke-width="4" stroke-linecap="round" stroke-linejoin="round"/>
    </svg>
    <svg class="gallery-arrow" style="left:241px;" width="22" height="34" viewBox="0 0 22 34" aria-hidden="true">
      <polyline points="4,3 18,17 4,31" fill="none" stroke="#fff" stroke-width="4" stroke-linecap="round" stroke-linejoin="round"/>
    </svg>
  </div>

  <footer class="abs site-footer">
    <ul class="footer-links" style="left:42px;">
      <li>Introduction</li>
      <li>Pricing</li>
      <li>Gallery</li>
      <li>Location</li>
      <li>Contact</li>
      <li>Picks</li>
    </ul>
    <ul class="footer-links" style="left:221px;">
      <li>Terms &amp; Conditions</li>
      <li>Legal Notice</li>
      <li>Disclaimer</li>
    </ul>
    <div class="footer-contact">
      <div class="footer-heading">VASKEMETSA PUHKEMAJA</div>
      <div>Metsa talu, Kivi küla, Rannu vald,</div>
      <div>Harjumaa 74810</div>
      <div>Tel. +372 55 12 340</div>
      <div>&nbsp;e-mail: info@vaskemetsa.ee</div>
    </div>
    <div class="social">
      <div class="footer-heading">Connect With Us</div>
      <div class="social-icons">
        <span class="social-icon" role="img" aria-label="Video channel"></span>
        <span class="social-icon" role="img" aria-label="News feed"></span>
        <span class="social-icon" role="img" aria-label="Social network"></span>
        <span class="social-icon" role="img" aria-label="Microblog"></span>
        <span class="social-icon" role="img" aria-label="Community page"></span>
      </div>
    </div>
    <div class="copyright">© 2014 Company Name ,All Rights Reserved</div>
  </footer>

</body>
</html>
```